My Web Development Portfolio site

I'm a web developer and I need a web design that can showcase my web development portfolio. I like most of the websites from this link: http://www.pixelmarrow.com/portfolios/examples-594821. My ideal design should be modern, clean and fun. I will let the designer decided the color theme for the website.

Target Market(s)

Potential Employers.

Number of Pages Required

1 page

Requirements
Must have
• - Menu bar that includes at least: About Me, Blog, Contact, Project/Work
• - Excellent color theme
• - Use the logo I provided (see attachment)
Nice to have
• - Some animation
• - Fun yet modern design

```html
<!DOCTYPE html>
<html lang="en">
<head>
<meta charset="utf-8">
<title>Byte Trail — Web Developer Portfolio</title>
<link href="https://fonts.googleapis.com/css2?family=Raleway:wght@300;400;600;700&family=Open+Sans:wght@400;600&display=swap" rel="stylesheet">
<style>
:root{
  --orange:#f0854a;
  --orange-dark:#e0733a;
  --ink:#333333;
  --muted:#888888;
  --light:#f4f4f4;
  --dark:#2b2b2b;
  --footer:#1f1f1f;
  --white:#ffffff;
}
*{box-sizing:border-box;margin:0;padding:0}
html,body{width:1200px;height:3044px;overflow:hidden}
body{font-family:"Open Sans",sans-serif;color:var(--ink);background:var(--white);position:relative}

/* hero */
.hero{position:absolute;left:0;top:0;width:1200px;height:620px;
  clip-path:polygon(0 0,100% 0,100% 540px,50% 620px,0 540px)}
.hero-photo{position:absolute;inset:0;background:linear-gradient(160deg,#5a5550 0%,#3b3734 45%,#2a2624 100%)}
.hero-shade{position:absolute;inset:0;background:rgba(20,20,20,.35)}
.main-nav{position:absolute;top:22px;left:0;width:100%;display:flex;justify-content:center;gap:34px}
.main-nav a{color:var(--white);font-size:12px;text-decoration:none;letter-spacing:.5px;text-transform:uppercase;font-family:"Raleway",sans-serif;font-weight:600}
.hero-brand{position:absolute;top:220px;left:0;width:100%;text-align:center;color:var(--white)}
.brand-name{font-family:"Raleway",sans-serif;font-weight:600;font-size:34px;letter-spacing:4px;text-transform:uppercase;line-height:1}
.hero-title{font-family:"Raleway",sans-serif;font-weight:600;font-size:44px;letter-spacing:2px;margin-top:26px}
.slide-arrow{position:absolute;top:284px;width:24px;height:40px}
.slide-arrow.prev{left:28px}
.slide-arrow.next{right:28px}

/* section titles */
.section-title{text-align:center;font-family:"Raleway",sans-serif;font-weight:400}
.title-rule{display:flex;align-items:center;justify-content:center;gap:10px;margin-top:10px}
.title-rule span{display:block;width:60px;height:1px;background:var(--orange)}
.title-rule i{display:block;width:18px;height:18px;border-radius:50%;border:3px solid var(--orange)}

/* welcome */
.welcome{position:absolute;top:672px;left:0;width:1200px;text-align:center}
.welcome h1{font-size:40px;color:var(--ink)}
.welcome .tagline{font-size:17px;color:var(--muted);margin-top:18px}
.welcome p.intro{width:820px;margin:14px auto 0;font-size:12.5px;line-height:20px;color:var(--muted)}

/* services band */
.services{position:absolute;top:950px;left:0;width:1200px;height:178px;background:var(--orange);display:flex;justify-content:center;gap:60px;padding-top:48px}
.service{width:130px;text-align:center;color:var(--white)}
.service svg{width:44px;height:40px}
.service span{display:block;font-size:13px;margin-top:10px;white-space:nowrap}

/* blog */
.blog{position:absolute;top:1160px;left:0;width:1200px}
.blog h2{font-size:30px;font-weight:600;color:var(--ink)}
.blog-cards{position:absolute;top:110px;left:100px;display:flex;gap:40px}
.blog-card{width:304px}
.blog-image{position:relative;height:192px;border-radius:2px}
.blog-card:nth-child(1) .blog-image{background:linear-gradient(135deg,#c98a62,#8d6a55 60%,#5c4a40)}
.blog-card:nth-child(2) .blog-image{background:linear-gradient(135deg,#7d7468,#a69a88 55%,#4e4a44)}
.blog-card:nth-child(3) .blog-image{background:linear-gradient(135deg,#d89a6a,#9aa3a8 55%,#6f7478)}
.date-badge{position:absolute;top:0;left:14px;width:46px;height:54px;background:var(--orange);color:var(--white);text-align:center;font-size:11px;line-height:14px;padding-top:8px}
.date-badge b{display:block;font-size:18px;line-height:22px}
.blog-card h3{font-family:"Raleway",sans-serif;font-size:16px;font-weight:600;margin-top:24px;color:var(--ink)}
.blog-meta{display:flex;gap:28px;font-size:11px;color:var(--muted);margin-top:12px}
.blog-meta span::before{content:"";display:inline-block;width:8px;height:8px;border:1px solid var(--orange);border-radius:50%;margin-right:6px;vertical-align:-1px}
.blog-card p{font-size:11.5px;line-height:17px;color:var(--muted);margin-top:10px}

/* projects */
.projects{position:absolute;top:1680px;left:0;width:1200px;height:660px;
  clip-path:polygon(0 20px,50% 0,100% 20px,100% 610px,50% 660px,0 610px)}
.projects-bg{position:absolute;inset:0;background:linear-gradient(180deg,#262626,#353535 50%,#2a2a2a)}
.projects h2{position:absolute;top:64px;left:0;width:100%;color:var(--white);font-size:30px;font-weight:600}
.projects .title-rule{position:absolute;top:108px;left:0;width:100%}
.project-grid{position:absolute;top:168px;left:100px;display:grid;grid-template-columns:368px 300px 300px;grid-template-rows:200px 204px;gap:16px}
.project{border:3px solid rgba(255,255,255,.12)}
.project.feature{grid-row:1 / span 2;background:linear-gradient(160deg,#a8a8a8,#6e6e70 60%,#4d4d50)}
.project.p2{background:linear-gradient(135deg,#7b6a52,#c8a25a 60%,#5a4b3a)}
.project.p3{background:linear-gradient(135deg,#c69a6c,#8a9a92 60%,#5f6c60)}
.project.p4{background:linear-gradient(135deg,#6f8a96,#a7a49a 55%,#5d5a55)}
.project.p5{background:linear-gradient(135deg,#c9c6c0,#8f8c86 60%,#5e5c58)}

/* contact */
.contact{position:absolute;top:2360px;left:0;width:1200px;height:520px}
.contact-brand{position:absolute;top:44px;left:0;width:100%;text-align:center}
.contact-brand .brand-name{font-size:28px;color:var(--orange)}
.contact-form{position:absolute;top:128px;left:100px;width:700px;display:grid;grid-template-columns:370px 300px;gap:14px 30px}
.field-col{display:flex;flex-direction:column;gap:14px}
.field{height:48px;border:1px solid #dddddd;border-radius:2px;font-size:11px;color:var(--muted);padding:10px 12px}
.field.message{height:176px}
.submit{align-self:flex-end;width:100px;height:44px;background:var(--orange);color:var(--white);font-size:12px;display:flex;align-items:center;justify-content:center;text-transform:uppercase}
.contact-info{position:absolute;top:128px;left:848px;width:260px}
.contact-info h2{font-family:"Raleway",sans-serif;font-size:34px;font-weight:400;color:var(--ink)}
.info-row{display:flex;gap:16px;margin-top:26px;font-size:11.5px;line-height:16px;color:var(--muted)}
.info-icon{flex:none;width:30px;height:30px;border-radius:50%;background:var(--dark);display:flex;align-items:center;justify-content:center}
.info-icon svg{width:14px;height:14px}

/* footer */
.site-footer{position:absolute;top:2880px;left:0;width:1200px;height:164px;background:var(--footer);text-align:center;color:#bbbbbb}
.social{display:flex;justify-content:center;gap:12px;padding-top:40px}
.social i{display:block;width:30px;height:30px;border-radius:50%;background:var(--white)}
.footer-nav{display:flex;justify-content:center;gap:26px;margin-top:18px}
.footer-nav a{color:#dddddd;font-size:11px;text-decoration:none;text-transform:uppercase;font-family:"Raleway",sans-serif;font-weight:600}
.copyright{font-size:10.5px;margin-top:14px;color:#999999}
.to-top{position:absolute;right:30px;top:112px;width:20px;height:20px}
</style>
</head>
<body>

<header class="hero">
  <div class="hero-photo" role="img" aria-label="Photo of a developer working at a desk in a bright office"></div>
  <div class="hero-shade"></div>
  <nav class="main-nav">
    <a href="#">Home</a><a href="#">About Me</a><a href="#">Blog</a><a href="#">Project/Work</a><a href="#">Contact</a>
  </nav>
  <svg class="slide-arrow prev" viewBox="0 0 24 40"><polyline points="20,4 4,20 20,36" fill="none" stroke="#ffffff" stroke-opacity=".6" stroke-width="3"/></svg>
  <svg class="slide-arrow next" viewBox="0 0 24 40"><polyline points="4,4 20,20 4,36" fill="none" stroke="#ffffff" stroke-opacity=".6" stroke-width="3"/></svg>
  <div class="hero-brand">
    <div class="brand-name">Byte Trail</div>
    <div class="hero-title">I'M A WEB DEVELOPER</div>
  </div>
</header>

<section class="welcome">
  <h1 class="section-title">Welcome To Byte Trail</h1>
  <div class="title-rule"><span></span><i></i><span></span></div>
  <div class="tagline">I'm a web developer</div>
  <p class="intro">We build fast, clean and friendly websites for people who care about detail. Every project starts with listening, then sketching, then careful code that works on every screen. I enjoy solving hard problems with simple ideas, and I like to keep things light and fun along the way. Browse my latest posts and projects below, and feel free to drop me a line any time.</p>
</section>

<section class="services">
  <div class="service">
    <svg viewBox="0 0 44 40"><rect x="3" y="3" width="38" height="25" rx="2" fill="none" stroke="#fff" stroke-width="3"/><rect x="18" y="28" width="8" height="6" fill="#fff"/><rect x="12" y="34" width="20" height="3" fill="#fff"/></svg>
    <span>Web Development</span>
  </div>
  <div class="service">
    <svg viewBox="0 0 44 40"><path d="M8 34 L30 6 L36 11 L14 38 L6 39 Z" fill="#fff"/></svg>
    <span>Branding</span>
  </div>
  <div class="service">
    <svg viewBox="0 0 44 40"><polyline points="4,36 4,4" stroke="#fff" stroke-width="3" fill="none"/><polyline points="4,36 42,36" stroke="#fff" stroke-width="3" fill="none"/><polyline points="8,30 18,18 26,24 40,8" stroke="#fff" stroke-width="3" fill="none"/></svg>
    <span>Web Design</span>
  </div>
  <div class="service">
    <svg viewBox="0 0 44 40"><path d="M4 12 H14 L17 6 H27 L30 12 H40 V36 H4 Z" fill="#fff"/><circle cx="22" cy="23" r="8" fill="#f0854a"/><circle cx="22" cy="23" r="5" fill="#fff"/></svg>
    <span>Photography</span>
  </div>
  <div class="service">
    <svg viewBox="0 0 44 40"><path d="M7 26 V20 A15 15 0 0 1 37 20 V26" fill="none" stroke="#fff" stroke-width="3"/><rect x="4" y="24" width="9" height="13" rx="2" fill="#fff"/><rect x="31" y="24" width="9" height="13" rx="2" fill="#fff"/></svg>
    <span>Live Support</span>
  </div>
</section>

<section class="blog">
  <h2 class="section-title">LATEST BLOG</h2>
  <div class="title-rule"><span></span><i></i><span></span></div>
  <div class="blog-cards">
    <article class="blog-card">
      <div class="blog-image" role="img" aria-label="Photo of hands using a laptop and tablet on a desk"><div class="date-badge">APR<b>02</b></div></div>
      <h3>Nemo enim ipsam voluptatem</h3>
      <div class="blog-meta"><span>web developer</span><span>No comments</span></div>
      <p>A short look at how I plan layouts, pick colours and write tidy code for small business sites that load fast.</p>
    </article>
    <article class="blog-card">
      <div class="blog-image" role="img" aria-label="Photo of a man looking at his phone in a cafe"><div class="date-badge">APR<b>02</b></div></div>
      <h3>Nemo enim ipsam voluptatem</h3>
      <div class="blog-meta"><span>web developer</span><span>No comments</span></div>
      <p>A short look at how I plan layouts, pick colours and write tidy code for small business sites that load fast.</p>
    </article>
    <article class="blog-card">
      <div class="blog-image" role="img" aria-label="Photo of a hand holding a smartphone on a city street"><div class="date-badge">APR<b>02</b></div></div>
      <h3>Nemo enim ipsam voluptatem</h3>
      <div class="blog-meta"><span>web developer</span><span>No comments</span></div>
      <p>A short look at how I plan layouts, pick colours and write tidy code for small business sites that load fast.</p>
    </article>
  </div>
</section>

<section class="projects">
  <div class="projects-bg" role="img" aria-label="Dark blurred photo of a workspace"></div>
  <h2 class="section-title">PROJECT/WORK</h2>
  <div class="title-rule"><span></span><i></i><span></span></div>
  <div class="project-grid">
    <div class="project feature" role="img" aria-label="Photo of a man in a suit holding a tablet with app icons floating above it"></div>
    <div class="project p2" role="img" aria-label="Photo of a laptop on a wooden desk"></div>
    <div class="project p3" role="img" aria-label="Photo of a team working together at a table"></div>
    <div class="project p4" role="img" aria-label="Photo of a laptop with charts and notes"></div>
    <div class="project p5" role="img" aria-label="Photo of a man working on a laptop outdoors"></div>
  </div>
</section>

<section class="contact">
  <div class="contact-brand">
    <div class="brand-name">Byte Trail</div>
  </div>
  <form class="contact-form">
    <div class="field-col">
      <div class="field">Name</div>
      <div class="field">Email</div>
      <div class="field">Phone</div>
      <div class="field">Subject</div>
    </div>
    <div class="field-col">
      <div class="field message">Message</div>
      <div class="submit">Submit</div>
    </div>
  </form>
  <div class="contact-info">
    <h2>Contact Us</h2>
    <div class="info-row">
      <span class="info-icon"><svg viewBox="0 0 14 14"><path d="M7 1 A4.5 4.5 0 0 1 11.5 5.5 C11.5 9 7 13 7 13 C7 13 2.5 9 2.5 5.5 A4.5 4.5 0 0 1 7 1 Z" fill="#fff"/><circle cx="7" cy="5.5" r="1.6" fill="#2b2b2b"/></svg></span>
      <span>27 Maple Lane, Suite 4<br>Lakeview, LA 70120</span>
    </div>
    <div class="info-row">
      <span class="info-icon"><svg viewBox="0 0 14 14"><path d="M3 1 L5.5 1 L6.5 4 L5 5.2 C5.8 7 7 8.2 8.8 9 L10 7.5 L13 8.5 L13 11 C13 12 12 13 11 13 C5.5 13 1 8.5 1 3 C1 2 2 1 3 1 Z" fill="#fff"/></svg></span>
      <span>Call Us<br>(+1) 318.555.0142</span>
    </div>
    <div class="info-row">
      <span class="info-icon"><svg viewBox="0 0 14 14"><rect x="1" y="3" width="12" height="8" fill="#fff"/><polyline points="1,3 7,8 13,3" fill="none" stroke="#2b2b2b" stroke-width="1.2"/></svg></span>
      <span>E - Mail<br>info@bytetrail.dev</span>
    </div>
  </div>
</section>

<footer class="site-footer">
  <div class="social"><i></i><i></i><i></i><i></i><i></i></div>
  <nav class="footer-nav">
    <a href="#">Home</a><a href="#">About Us</a><a href="#">Blog</a><a href="#">Project/Work</a><a href="#">Contact</a>
  </nav>
  <div class="copyright">2016 © Byte Trail All Rights Reserved</div>
  <svg class="to-top" viewBox="0 0 20 20"><polyline points="4,13 10,7 16,13" fill="none" stroke="#888" stroke-width="2"/></svg>
</footer>

</body>
</html>
```